Business Card Re-Design for a Lighting Designer

I would like my business card re-designed. It is currently high gloss and they scratch too easily. I don not think the current design lends itself well to a matte finish. I have included the current design for reference along with our company logo.
Check out our website for current branding.
http://www.brambleorchidstudio.example

Updates
Some of the top contenders are muslim and it is a holiday for them. I do not want to discriminate and would expect the same courtesy for holidays we celebrate.
Target Market(s)
Interior Designers, Architects
Contact Information for Business Card
Logo - Name, Title, Address, Telephone Number and Extension, Email
Font styles to use
Requirements
Must have
- All the information listed on the current business card. If you use Red, it needs to be the red from our logo.
Nice to have
- Vertical and Horizontal Designs will be entertained.
Should not have
- Requirements for a glossy finish...should not look too corporate since we are a design firm.

```html
<!DOCTYPE html>
<html lang="en">
<head>
<meta charset="utf-8">
<title>Bramble Orchid Studio – Business Card</title>
<link rel="stylesheet" href="https://fonts.googleapis.com/css2?family=Roboto+Condensed:wght@300;700&family=Roboto:wght@400&display=swap">
<style>
  :root {
    --backdrop: #e3dddd;
    --card-dark: #242424;
    --card-light: #ffffff;
    --ink-light: #ffffff;
  }
  * { margin: 0; padding: 0; box-sizing: border-box; }
  html, body { width: 1200px; height: 1000px; overflow: hidden; }
  body { background: var(--backdrop); position: relative; }

  .card {
    position: absolute;
    left: 224px;
    width: 752px;
    height: 430px;
    background: var(--card-dark);
    overflow: hidden;
  }
  .card--front { top: 56px; }
  .card--back { top: 514px; }

  .card__wedge { position: absolute; inset: 0; width: 100%; height: 100%; }
  .card__wedge polygon { fill: var(--card-light); }

  /* Front: brand name */
  .brand {
    position: absolute;
    left: 277px;
    top: 109px;
    width: 200px;
  }
  .brand__square {
    width: 96px;
    height: 96px;
    background: var(--ink-light);
    margin-bottom: 16px;
  }
  .brand__name {
    font-family: "Roboto Condensed", sans-serif;
    font-weight: 300;
    font-size: 38px;
    line-height: 38px;
    color: var(--ink-light);
    text-transform: uppercase;
  }

  /* Back: contact details */
  .contact {
    position: absolute;
    left: 75px;
    top: 0;
    color: var(--ink-light);
  }
  .contact__name {
    position: absolute;
    top: 62px;
    white-space: nowrap;
    font-family: "Roboto Condensed", sans-serif;
    font-weight: 700;
    font-size: 40px;
    line-height: 40px;
  }
  .contact__title {
    position: absolute;
    top: 110px;
    font-family: "Roboto Condensed", sans-serif;
    font-weight: 700;
    font-size: 25px;
    line-height: 25px;
  }
  .contact__block {
    position: absolute;
    white-space: nowrap;
    font-family: "Roboto", sans-serif;
    font-weight: 400;
    font-size: 25px;
    line-height: 33px;
    letter-spacing: 0.5px;
  }
  .contact__address { top: 160px; }
  .contact__lines { top: 268px; }
</style>
</head>
<body>
  <section class="card card--front">
    <svg class="card__wedge" viewBox="0 0 752 430" preserveAspectRatio="none" aria-hidden="true">
      <polygon points="0,0 163,430 0,430"/>
    </svg>
    <div class="brand">
      <div class="brand__square"></div>
      <p class="brand__name">Bramble<br>Orchid<br>Studio</p>
    </div>
  </section>

  <section class="card card--back">
    <svg class="card__wedge" viewBox="0 0 752 430" preserveAspectRatio="none" aria-hidden="true">
      <polygon points="589,0 752,0 752,430"/>
    </svg>
    <div class="contact">
      <h1 class="contact__name">MAREN CALLOWAY</h1>
      <p class="contact__title">PRINCIPAL</p>
      <p class="contact__block contact__address">217 Linden Crossing, Suite 40<br>Marlow, Oregon 97001 USA</p>
      <p class="contact__block contact__lines">555.014.2290x1<br>maren@brambleorchidstudio.example<br>www.brambleorchidstudio.example</p>
    </div>
  </section>
</body>
</html>
```